2019 Chase the Morning Comet (Cardio Calendar)

I would like to put together a calendar of cardio workouts for the year. I would have 4 different workouts per week + 2 basic steady state workouts. I envision a picture of me on the top page and along with the challenge of the month description and the 3 different types of cardio description. on the bottom page would be the calendar for that month with the workout typed into the box. I am not sure if a boxed calendar would be enough space to write each workout in so I am open to more ideas on how to present the workouts

Target Market(s)

Women 20-60 years old
moms
couples
men
athletes

Industry/Entity Type

Fitness

Font styles to use
Sans Serif

Colors

Designer to choose colors to be used in the design.

Requirements
Must have
• Ability to incorporate 4 different workouts per week in a downloadable calendar style
• I want to have a different picture available for each month
• modern, bold, but simple and clean presentation
Nice to have
• picture at the top, with a description of the 3 different types of workouts for that month.
• On the bottom would be space for separate days of each workout
Should not have
• NA

```html
<!DOCTYPE html>
<html lang="en">
<head>
<meta charset="utf-8">
<title>Chase the Morning Comet – January 2019</title>
<link rel="stylesheet" href="https://fonts.googleapis.com/css2?family=Roboto+Condensed:wght@300;400;700&display=swap">
<style>
  :root {
    --paper: #f6f6f4;
    --red: #d8261c;
    --ink: #2b2b2b;
    --muted: #555555;
    --grid: #c9c9c9;
    --head-bg: #dddddd;
    --rest: #3b6ea8;
    --rule: #c4c4c4;
  }
  * { margin: 0; padding: 0; box-sizing: border-box; }
  html, body { width: 724px; height: 1200px; overflow: hidden; background: var(--paper); }
  body { font-family: "Roboto Condensed", Arial, sans-serif; color: var(--ink); position: relative; }

  .hero-photo {
    position: absolute; left: 0; top: 0; width: 724px; height: 357px;
    background:
      linear-gradient(180deg, #0b0f14 0%, #121a22 55%, #1c2a1c 72%, #2f6a22 84%, #3c7f2a 100%);
  }
  .month-badge {
    position: absolute; left: 218px; top: 330px; width: 288px; height: 54px;
    background: var(--red); border-radius: 27px;
    display: flex; align-items: center; justify-content: center;
    color: #fff; font-weight: 700; font-size: 31px; letter-spacing: 0.5px;
  }

  .challenge { position: absolute; left: 41px; top: 424px; width: 640px; }
  .challenge h2 { font-weight: 400; font-size: 23px; color: #3a3a3a; }
  .challenge p { margin-top: 6px; font-weight: 300; font-size: 8.4px; line-height: 12px; color: var(--muted); }

  .calendar {
    position: absolute; left: 42px; top: 510px; width: 640px;
    display: grid; grid-template-columns: repeat(7, 1fr);
    border-left: 1px solid var(--grid); border-top: 1px solid var(--grid);
  }
  .weekday {
    height: 34px; background: var(--head-bg);
    border-right: 1px solid var(--grid); border-bottom: 1px solid var(--grid);
    display: flex; align-items: center; justify-content: center;
    font-size: 17px; color: #333;
  }
  .day {
    position: relative; height: 91.5px;
    border-right: 1px solid var(--grid); border-bottom: 1px solid var(--grid);
    text-align: center; font-size: 11.5px; line-height: 15px;
  }
  .day-number {
    position: absolute; left: 0; top: 0; width: 30px; height: 30px;
    background: var(--red); border-bottom-right-radius: 30px;
    color: #fff; font-weight: 700; font-size: 11px; line-height: 11px;
    padding: 7px 0 0 6px; text-align: left;
  }
  .day.outside .day-number { background: none; color: #ececec; }
  .workout { padding-top: 30px; }
  .workout strong { display: block; font-weight: 700; color: #222; }
  .workout span { display: block; font-weight: 400; color: #444; }
  .day.rest .workout { color: var(--rest); font-weight: 700; letter-spacing: 0.3px; }

  .notes { position: absolute; left: 47px; top: 1051px; width: 630px; }
  .notes hr { border: 0; border-top: 1px solid var(--rule); height: 26.5px; }
</style>
</head>
<body>
  <div class="hero-photo" role="img" aria-label="Photo of an athlete stretching with a foam roller on a dark, floodlit turf field"></div>
  <div class="month-badge">JANUARY 2019</div>

  <section class="challenge">
    <h2>Challenge of the month</h2>
    <p>Lorem ipsum dolor sit amet, consectetur adipiscing elit. Nam lobortis magna ut libero feugiat, euismod commodo risus scelerisque. Suspendisse fermentum risus ut fermentum porttitor. Vivamus dolor mauris, fermentum non augue placerat, cursus pellentesque ex.</p>
  </section>

  <section class="calendar">
    <div class="weekday">SUNDAY</div><div class="weekday">MONDAY</div><div class="weekday">TUESDAY</div><div class="weekday">WEDNESDAY</div><div class="weekday">THURSDAY</div><div class="weekday">FRIDAY</div><div class="weekday">SATURDAY</div>

    <div class="day outside"><div class="day-number">30</div></div>
    <div class="day outside"><div class="day-number">31</div></div>
    <div class="day"><div class="day-number">1</div><div class="workout"><strong>Cardio</strong><span>Exercise #2</span></div></div>
    <div class="day"><div class="day-number">2</div><div class="workout"><strong>Cardio</strong><span>Exercise #3</span></div></div>
    <div class="day"><div class="day-number">3</div><div class="workout"><strong>Cardio</strong><span>Exercise #4</span></div></div>
    <div class="day"><div class="day-number">4</div><div class="workout"><strong>Basic</strong><span>Exercise #1</span></div></div>
    <div class="day"><div class="day-number">5</div><div class="workout"><strong>Basic</strong><span>Exercise #2</span></div></div>

    <div class="day rest"><div class="day-number">06</div><div class="workout">TAKE<br>REST</div></div>
    <div class="day"><div class="day-number">7</div><div class="workout"><strong>Cardio</strong><span>Exercise #1</span></div></div>
    <div class="day"><div class="day-number">8</div><div class="workout"><strong>Cardio</strong><span>Exercise #2</span></div></div>
    <div class="day"><div class="day-number">9</div><div class="workout"><strong>Cardio</strong><span>Exercise #3</span></div></div>
    <div class="day"><div class="day-number">10</div><div class="workout"><strong>Cardio</strong><span>Exercise #4</span></div></div>
    <div class="day"><div class="day-number">11</div><div class="workout"><strong>Basic</strong><span>Exercise #1</span></div></div>
    <div class="day"><div class="day-number">12</div><div class="workout"><strong>Basic</strong><span>Exercise #2</span></div></div>

    <div class="day rest"><div class="day-number">13</div><div class="workout">TAKE<br>REST</div></div>
    <div class="day"><div class="day-number">14</div><div class="workout"><strong>Cardio</strong><span>Exercise #1</span></div></div>
    <div class="day"><div class="day-number">15</div><div class="workout"><strong>Cardio</strong><span>Exercise #2</span></div></div>
    <div class="day"><div class="day-number">16</div><div class="workout"><strong>Cardio</strong><span>Exercise #3</span></div></div>
    <div class="day"><div class="day-number">17</div><div class="workout"><strong>Cardio</strong><span>Exercise #4</span></div></div>
    <div class="day"><div class="day-number">18</div><div class="workout"><strong>Basic</strong><span>Exercise #1</span></div></div>
    <div class="day"><div class="day-number">19</div><div class="workout"><strong>Basic</strong><span>Exercise #2</span></div></div>

    <div class="day rest"><div class="day-number">20</div><div class="workout">TAKE<br>REST</div></div>
    <div class="day"><div class="day-number">21</div><div class="workout"><strong>Cardio</strong><span>Exercise #1</span></div></div>
    <div class="day"><div class="day-number">22</div><div class="workout"><strong>Cardio</strong><span>Exercise #2</span></div></div>
    <div class="day"><div class="day-number">23</div><div class="workout"><strong>Cardio</strong><span>Exercise #3</span></div></div>
    <div class="day"><div class="day-number">24</div><div class="workout"><strong>Cardio</strong><span>Exercise #4</span></div></div>
    <div class="day"><div class="day-number">25</div><div class="workout"><strong>Basic</strong><span>Exercise #1</span></div></div>
    <div class="day"><div class="day-number">26</div><div class="workout"><strong>Basic</strong><span>Exercise #2</span></div></div>

    <div class="day rest"><div class="day-number">27</div><div class="workout">TAKE<br>REST</div></div>
    <div class="day"><div class="day-number">28</div><div class="workout"><strong>Cardio</strong><span>Exercise #1</span></div></div>
    <div class="day"><div class="day-number">29</div><div class="workout"><strong>Cardio</strong><span>Exercise #2</span></div></div>
    <div class="day"><div class="day-number">30</div><div class="workout"><strong>Cardio</strong><span>Exercise #3</span></div></div>
    <div class="day"><div class="day-number">31</div><div class="workout"><strong>Cardio</strong><span>Exercise #4</span></div></div>
    <div class="day empty"></div>
    <div class="day empty"></div>
  </section>

  <section class="notes" aria-label="Notes">
    <hr><hr><hr><hr><hr>
  </section>
</body>
</html>
```